BrivaPop Popcorn Sell Sheet

I need to create a sell sheet for my pre-popped and packaged popcorn that I sell to distributors, grocery stores, and various other retail outlets. The sell sheet will be a presentation sheet that I can send to corporate retail buyers and category managers describing my product, and the benefits to selling it in their stores or through their distributor network.

```html
<!DOCTYPE html>
<html lang="en">
<head>
<meta charset="UTF-8">
<title>BrivaPop Popcorn – Sell Sheet</title>
<link href="https://fonts.googleapis.com/css2?family=Fira+Sans:wght@500;600;700&family=Montserrat:wght@800;900&display=swap" rel="stylesheet">
<style>
  :root {
    --navy: #17478a;
    --sun: #f9c80e;
    --sky: #66acdc;
    --sky-light: #9ccbeb;
    --white: #ffffff;
    --stage: #c4c4c4;
    --wash: #d7ebf7;
  }
  * { margin: 0; padding: 0; box-sizing: border-box; }
  html, body { width: 1200px; height: 1117px; overflow: hidden; background: var(--stage); }
  body { font-family: "Fira Sans", sans-serif; color: var(--navy); position: relative; }

  .sell-sheet {
    position: absolute; left: 0; top: 95px; width: 1200px; height: 927px;
    background:
      radial-gradient(ellipse 420px 200px at 1060px 40px, var(--wash), transparent 70%),
      radial-gradient(ellipse 380px 90px at 620px 0px, #e6f2fa, transparent 70%),
      var(--white);
    overflow: hidden;
  }
  .headline {
    position: absolute; left: 62px; top: 40px;
    font-family: "Montserrat", sans-serif; font-weight: 900;
    font-size: 119px; letter-spacing: -2px; line-height: 1;
    white-space: nowrap;
  }
  .headline .accent { color: var(--sun); }
  .headline .main { color: var(--navy); }
  .tagline-bar {
    position: absolute; left: 64px; top: 163px; width: 879px; height: 50px;
    background: var(--sun); border-radius: 25px;
    display: flex; align-items: center; justify-content: center;
    font-weight: 700; font-size: 33px; color: var(--navy);
  }
  .lettering {
    position: absolute; border-radius: 14px;
    background: linear-gradient(120deg, #fbe08a, #6f94c6);
  }
  .lettering--top { left: 967px; top: 39px; width: 212px; height: 165px; transform: rotate(-14deg); }
  .lettering--side { left: 62px; top: 261px; width: 326px; height: 82px; }

  .brand-mark {
    position: absolute; left: 62px; top: 368px; width: 337px; height: 363px;
    display: flex; flex-direction: column; align-items: center; justify-content: center; gap: 28px;
  }
  .brand-mark .disc { width: 190px; height: 190px; border-radius: 50%; background: var(--sun); }
  .brand-mark .name { font-weight: 700; font-size: 58px; color: var(--navy); line-height: 1; text-align: center; }

  .product-photo {
    position: absolute; left: 414px; top: 242px; width: 372px; height: 548px;
    background: linear-gradient(180deg, #eeece8, #f7f6f2 40%, #e8e3da);
    z-index: 2;
  }

  .benefits {
    position: absolute; left: 815px; top: 246px; width: 385px; height: 287px;
    background: linear-gradient(100deg, var(--sky), var(--sky-light));
    border-radius: 30px 0 0 30px;
    color: var(--white);
  }
  .benefit { position: absolute; left: 31px; display: flex; align-items: flex-start; gap: 15px; }
  .benefit svg { flex: none; }
  .benefit span { font-weight: 600; font-size: 27px; line-height: 30px; }
  .benefit--one { top: 28px; }
  .benefit--two { top: 153px; align-items: center; }
  .benefit--three { top: 224px; align-items: center; }
  .benefit-rule { position: absolute; left: 31px; width: 288px; height: 1.5px; background: var(--white); }

  .availability {
    position: absolute; left: 820px; top: 550px; width: 340px;
    text-align: center; font-weight: 700; font-size: 31px; line-height: 35px;
  }
  .shop-link {
    position: absolute; left: 824px; top: 673px; width: 330px; height: 48px;
    border: 4px solid var(--sun); border-radius: 24px;
    display: flex; align-items: center; justify-content: center;
    font-weight: 700; font-size: 27px;
  }

  .waves { position: absolute; left: 0; top: 0; width: 1200px; height: 927px; z-index: 1; }
  .contact-bar {
    position: absolute; left: 0; top: 855px; width: 1200px;
    display: flex; justify-content: center; align-items: center; gap: 15px;
    color: var(--white); font-weight: 600; font-size: 28px; z-index: 3;
  }
  .contact-bar .item { display: flex; align-items: center; gap: 9px; }
  .contact-bar .divider { width: 2px; height: 32px; background: var(--white); }
</style>
</head>
<body>
<main class="sell-sheet">
  <h1 class="headline"><span class="accent">ALL</span> <span class="main">NATURAL</span></h1>
  <div class="tagline-bar">Made Locally in SoCal</div>
  <div class="lettering lettering--top" role="img" aria-label="Hand-lettered script slogan in yellow and navy, tilted"></div>

  <div class="lettering lettering--side" role="img" aria-label="Hand-lettered script slogan in yellow and navy"></div>
  <div class="brand-mark">
    <div class="disc"></div>
    <div class="name">BrivaPop<br>Popcorn</div>
  </div>

  <div class="product-photo" role="img" aria-label="Photo of a clear bag of popped popcorn with a white front label, net weight 5 oz"></div>

  <section class="benefits">
    <div class="benefit benefit--one">
      <svg width="36" height="36" viewBox="0 0 36 36"><circle cx="18" cy="18" r="16" fill="none" stroke="#fff" stroke-width="2"/><path d="M14 9h8M16 9v8l-5 9h14l-5-9V9" fill="none" stroke="#fff" stroke-width="2"/></svg>
      <span>No Preservatives<br>Or Added<br>Ingredients</span>
    </div>
    <div class="benefit-rule" style="top:135px"></div>
    <div class="benefit benefit--two">
      <svg width="36" height="36" viewBox="0 0 36 36"><circle cx="18" cy="18" r="16" fill="none" stroke="#fff" stroke-width="2"/><path d="M8 28L28 8" stroke="#fff" stroke-width="2"/></svg>
      <span>Non-GMO Corn</span>
    </div>
    <div class="benefit-rule" style="top:202px"></div>
    <div class="benefit benefit--three">
      <svg width="36" height="36" viewBox="0 0 36 36"><circle cx="18" cy="18" r="16" fill="none" stroke="#fff" stroke-width="2"/><path d="M18 28V12M18 16l-4-4M18 16l4-4M18 21l-4-4M18 21l4-4M8 28L28 8" fill="none" stroke="#fff" stroke-width="2"/></svg>
      <span>Gluten Free</span>
    </div>
  </section>

  <p class="availability">Available at<br>many SoCal grocers<br>or online at</p>
  <div class="shop-link">brivapoppopcorn.com</div>

  <svg class="waves" viewBox="0 0 1638 1266" preserveAspectRatio="none" aria-hidden="true">
    <path d="M0 1150 C400 1030 900 1070 1638 1025 L1638 1266 L0 1266 Z" fill="#64acdb"/>
    <path d="M0 1162 C450 1060 950 1120 1638 1040 L1638 1266 L0 1266 Z" fill="#ffffff"/>
    <path d="M0 1175 C450 1080 950 1140 1638 1055 L1638 1266 L0 1266 Z" fill="#17478a"/>
  </svg>

  <footer class="contact-bar">
    <div class="item">
      <svg width="20" height="28" viewBox="0 0 20 28"><path d="M10 1C5 1 1 5 1 10c0 7 9 17 9 17s9-10 9-17c0-5-4-9-9-9z" fill="#fff"/><circle cx="10" cy="10" r="3.5" fill="#17478a"/></svg>
      Coastview, CA 92000
    </div>
    <span class="divider"></span>
    <div class="item">
      <svg width="26" height="26" viewBox="0 0 26 26"><circle cx="13" cy="13" r="12" fill="#fff"/><path d="M9 7l3 3-2 2c1 2 2 3 4 4l2-2 3 3-2 2c-5 0-10-5-10-10z" fill="#17478a"/></svg>
      619-555-0142
    </div>
    <span class="divider"></span>
    <div class="item">
      <svg width="26" height="26" viewBox="0 0 26 26"><circle cx="13" cy="13" r="12" fill="#fff"/><g fill="none" stroke="#17478a" stroke-width="1.4"><circle cx="13" cy="13" r="7"/><ellipse cx="13" cy="13" rx="3" ry="7"/><path d="M6 13h14M7 9.5h12M7 16.5h12"/></g></svg>
      www.brivapoppopcorn.com
    </div>
  </footer>
</main>
</body>
</html>
```